Refresh of Business Card Design

Want to refresh the business card design with the new logo while adhering to style guide as attached. Would like to match feel of website www.durmackvinex.com

```html
<!DOCTYPE html>
<html lang="en">
<head>
<meta charset="utf-8">
<title>Durmack Vinex — Business Card</title>
<link href="https://fonts.googleapis.com/css2?family=Montserrat:wght@400;500;700&display=swap" rel="stylesheet">
<style>
  :root {
    --stage: #4a4a4c;
    --card-black: #151515;
    --card-white: #ffffff;
    --brand-red: #d7202a;
    --ink-light: #f2f2f2;
    --ink-dark: #1a1a1a;
    --font-main: "Montserrat", Arial, sans-serif;
  }
  * { box-sizing: border-box; margin: 0; padding: 0; }
  html, body {
    width: 1200px; height: 1200px; overflow: hidden;
    background: var(--stage);
    font-family: var(--font-main);
  }
  .sheet {
    width: 1200px; height: 1200px;
    display: flex; flex-direction: column; align-items: center; justify-content: center;
    gap: 54px;
  }
  .card {
    position: relative;
    width: 880px; height: 503px;
    border-radius: 34px;
    overflow: hidden;
    background: var(--card-black);
    box-shadow: 0 14px 30px rgba(0,0,0,.45);
  }
  .card-front__backdrop { position: absolute; inset: 0; width: 100%; height: 100%; }
  .shape-black { fill: var(--card-black); }
  .shape-red { fill: var(--brand-red); }
  .shape-white { fill: var(--card-white); }
  .shape-gap { fill: none; stroke: var(--card-white); stroke-width: 3; }

  .brand-lockup {
    position: absolute;
    display: flex; align-items: center; gap: 14px;
    font-weight: 700; letter-spacing: 1px; white-space: nowrap;
  }
  .brand-lockup__dot { border-radius: 50%; background: var(--brand-red); flex: none; }
  .card-front .brand-lockup {
    left: 60px; top: 233px; font-size: 30px; color: var(--ink-dark);
  }
  .card-front .brand-lockup__dot { width: 34px; height: 34px; }

  .contact-block {
    position: absolute; left: 590px; top: 132px; width: 275px;
    color: var(--ink-light);
  }
  .contact-block__name {
    font-size: 38px; font-weight: 700; color: var(--brand-red);
    line-height: 1; letter-spacing: .5px; white-space: nowrap;
  }
  .contact-block__role {
    font-size: 20px; font-weight: 500; margin-top: 4px; letter-spacing: .5px;
  }
  .contact-list { list-style: none; margin-top: 18px; }
  .contact-list li {
    display: flex; align-items: flex-start; gap: 9px;
    font-size: 13px; line-height: 1.3; margin-bottom: 8px; white-space: nowrap;
  }
  .contact-icon { width: 16px; height: 16px; flex: none; }
  .icon-fill { fill: var(--brand-red); }
  .icon-line { fill: none; stroke: var(--brand-red); stroke-width: 1.4; }
  .icon-cut { fill: none; stroke: var(--card-black); stroke-width: 1.3; }
  .icon-hole { fill: var(--card-black); }

  .card-back .brand-lockup {
    left: 50%; top: 50%; transform: translate(-50%, -50%);
    font-size: 48px; color: var(--ink-light); letter-spacing: 2px; font-weight: 500;
    gap: 20px;
  }
  .card-back .brand-lockup__dot { width: 56px; height: 56px; }
</style>
</head>
<body>
<main class="sheet">

  <section class="card card-front" aria-label="Business card front">
    <svg class="card-front__backdrop" viewBox="0 0 880 503" preserveAspectRatio="none" aria-hidden="true">
      <rect class="shape-black" width="880" height="503"/>
      <path class="shape-red" d="M0 0 H395 C495 60 555 220 536 360 C527 420 508 470 490 503 H0 Z"/>
      <path class="shape-gap" d="M395 0 C495 60 555 220 536 360 C527 420 508 470 490 503"/>
      <path class="shape-white" d="M0 0 H340 C450 70 518 220 505 360 C498 420 482 470 464 503 H0 Z"/>
    </svg>

    <div class="brand-lockup">
      <span class="brand-lockup__dot"></span>
      <span>DURMACK VINEX</span>
    </div>

    <div class="contact-block">
      <p class="contact-block__name">FULL NAME</p>
      <p class="contact-block__role">POSITION</p>
      <ul class="contact-list">
        <li>
          <svg class="contact-icon" viewBox="0 0 16 16"><rect class="icon-line" x="4" y="1" width="8" height="14" rx="1.5"/><circle class="icon-fill" cx="8" cy="12.5" r="1"/></svg>
          <span>555.201.4830</span>
        </li>
        <li>
          <svg class="contact-icon" viewBox="0 0 16 16"><rect class="icon-fill" x="1" y="3.5" width="14" height="9"/><path class="icon-cut" d="M1 3.5 L8 9 L15 3.5"/></svg>
          <span>tmorrow@durmackvinex.com</span>
        </li>
        <li>
          <svg class="contact-icon" viewBox="0 0 16 16"><circle class="icon-line" cx="8" cy="8" r="6.5"/><ellipse class="icon-line" cx="8" cy="8" rx="3" ry="6.5"/><path class="icon-line" d="M1.5 8 H14.5 M2.5 4.8 H13.5 M2.5 11.2 H13.5"/></svg>
          <span>www.durmackvinex.com</span>
        </li>
        <li>
          <svg class="contact-icon" viewBox="0 0 16 16"><path class="icon-fill" d="M8 15 C4 10 3 8 3 6 A5 5 0 0 1 13 6 C13 8 12 10 8 15 Z"/><circle class="icon-hole" cx="8" cy="6" r="1.8"/></svg>
          <span>P.O. Box 48210 Ardenvale, TX 70011<br>72 Harlow Rd, Calverton, TX 70010</span>
        </li>
      </ul>
    </div>
  </section>

  <section class="card card-back" aria-label="Business card back">
    <div class="brand-lockup">
      <span class="brand-lockup__dot"></span>
      <span>DURMACK VINEX</span>
    </div>
  </section>

</main>
</body>
</html>
```